business card design and letterhead for a building inspection company. We have a pre-purchase building and pest inspection ( i inspect house before people purchase it)
Updates

Tilda has been so so responsive and good, i highly recommend her

Industry/Entity Type

Building

Contact Information for Business Card

audience, solicitor, real estate agent, mortgage brokerthe rest of the info will be in the attachement business card

```html
<!DOCTYPE html>
<html lang="en">
<head>
<meta charset="utf-8">
<title>Truehold Property Inspections – Business Card</title>
<link href="https://fonts.googleapis.com/css2?family=Montserrat:wght@400;500;600;700&display=swap" rel="stylesheet">
<style>
  :root {
    --stage: #202022;
    --card: #ffffff;
    --brand-blue: #1f7fc8;
    --ink: #111418;
    --card-shadow: rgba(0, 0, 0, 0.45);
  }
  * { box-sizing: border-box; margin: 0; padding: 0; }
  html, body {
    width: 1200px;
    height: 900px;
    overflow: hidden;
    background: var(--stage);
    font-family: "Montserrat", Arial, sans-serif;
  }
  .stage {
    position: relative;
    width: 1200px;
    height: 900px;
  }
  .card {
    position: absolute;
    width: 560px;
    height: 320px;
    background: var(--card);
    box-shadow: 0 18px 40px var(--card-shadow);
    overflow: hidden;
  }
  .card__band {
    position: absolute;
    left: 0; right: 0; bottom: 0;
    height: 14px;
    background: var(--brand-blue);
  }

  .brand {
    display: flex;
    align-items: center;
    gap: 10px;
  }
  .brand__dot {
    width: 14px;
    height: 14px;
    border-radius: 50%;
    background: var(--brand-blue);
    flex: none;
  }
  .brand__name {
    color: var(--brand-blue);
    font-weight: 700;
    font-size: 30px;
    letter-spacing: 1px;
    line-height: 1;
  }
  .brand__sub {
    color: var(--ink);
    font-weight: 500;
    font-size: 11px;
    letter-spacing: 0.5px;
    margin-top: 6px;
  }
  .brand__tagline {
    color: var(--brand-blue);
    font-size: 10px;
    letter-spacing: 1px;
    margin-top: 3px;
  }

  /* Contact side */
  .card--contact { left: 380px; top: 110px; }
  .card--contact .brand-block {
    position: absolute;
    left: 48px; top: 48px;
  }
  .person {
    position: absolute;
    left: 48px; top: 138px;
  }
  .person__name {
    color: var(--brand-blue);
    font-size: 22px;
    font-weight: 500;
    margin-bottom: 10px;
  }
  .contact-list { list-style: none; font-size: 12px; line-height: 1.45; color: var(--ink); }
  .contact-list__label { color: var(--brand-blue); }
  .website {
    position: absolute;
    left: 48px; bottom: 42px;
    font-size: 12px;
    font-weight: 500;
    color: var(--ink);
  }
  .corner-accent {
    position: absolute;
    right: 40px; top: 40px;
  }

  /* Brand side */
  .card--brand { left: 260px; top: 470px; }
  .card--brand .brand-block {
    position: absolute;
    left: 0; right: 0; top: 100px;
    display: flex;
    flex-direction: column;
    align-items: center;
  }
  .card--brand .brand__name { font-size: 38px; }
  .card--brand .brand__sub { font-size: 13px; }
  .card--brand .brand__tagline { font-size: 11px; }
  .services {
    position: absolute;
    left: 0; right: 0; top: 218px;
    text-align: center;
    font-size: 12px;
    color: var(--ink);
  }
</style>
</head>
<body>
<main class="stage">

  <section class="card card--contact">
    <div class="brand-block">
      <div class="brand">
        <span class="brand__name">TRUEHOLD</span>
      </div>
      <p class="brand__sub">PROPERTY INSPECTIONS</p>
      <p class="brand__tagline">Checked before you commit</p>
    </div>

    <svg class="corner-accent" width="150" height="150" viewBox="0 0 150 150" aria-hidden="true">
      <circle cx="75" cy="75" r="60" fill="none" stroke="var(--brand-blue)" stroke-width="12"/>
    </svg>

    <div class="person">
      <h1 class="person__name">Sarah Tilda</h1>
      <ul class="contact-list">
        <li><span class="contact-list__label">ph:</span> (02) 5550 1842</li>
        <li><span class="contact-list__label">mob:</span> 0400 555 218</li>
        <li><span class="contact-list__label">email:</span> info@trueholdinspections.com.au</li>
      </ul>
    </div>
    <p class="website">www.trueholdinspections.com.au</p>
    <div class="card__band"></div>
  </section>

  <section class="card card--brand">
    <div class="brand-block">
      <div class="brand">
        <span class="brand__dot"></span>
        <span class="brand__name">TRUEHOLD</span>
      </div>
      <p class="brand__sub">PROPERTY INSPECTIONS</p>
      <p class="brand__tagline">Checked before you commit</p>
    </div>
    <p class="services">Property Inspection / Property Maintenance</p>
    <div class="card__band"></div>
  </section>

</main>
</body>
</html>
```